Upmarket building and construction company needs signage

Our building company R Brent Construction, needs signage to put up on the side of our vehicle trailers and on site fencing. We are a building company that specialises in residential construction and carpentry .

I will attach our logo and some inspirational pics for site fencing as well as what our trailer looks like .
Other details i would like on the sign are our
( email) rbrentconstruction@mailbox-example.net
(mobile ) 0493 518 264
(website ) rbrentconstruction. example.net

Target Market(s)

Home owners looking for a reliable local builder who produces good quality work. I have attached some inspirational pics.

Industry/Entity Type

Building and Construction

Colors

Designer to choose colors to be used in the design.

Requirements
Must have
• Our logo, contact information
Nice to have
• We would like the design to have elements of being Elegant, Serious, Modern, Professional, Masculine, Conservative and Upmarket.

```html
<!DOCTYPE html>
<html lang="en">
<head>
<meta charset="utf-8">
<title>R Brent Construction – Site Signage</title>
<link rel="stylesheet" href="https://fonts.googleapis.com/css2?family=Open+Sans:wght@400;700;800&display=swap">
<style>
  :root {
    --canvas-bg: #e6e6e4;
    --sign-white: #ffffff;
    --roof-grey: #8f8f8f;
    --band-dark: #222222;
    --brand-grey: #7a7a7a;
    --text-light: #ffffff;
    --text-shadow: #1e1e1e;
  }
  * { margin: 0; padding: 0; box-sizing: border-box; }
  html, body {
    width: 1200px;
    height: 800px;
    overflow: hidden;
    background: var(--canvas-bg);
  }
  .canvas {
    position: relative;
    width: 1200px;
    height: 800px;
  }
  .sign {
    position: absolute;
    left: 26px;
    top: 148px;
    width: 1150px;
    height: 393px;
    background: var(--sign-white);
    overflow: hidden;
  }
  .sign-shapes {
    position: absolute;
    inset: 0;
    width: 1150px;
    height: 393px;
  }
  .brand {
    position: absolute;
    left: 96px;
    top: 118px;
    display: flex;
    align-items: flex-start;
    gap: 14px;
    font-family: "Open Sans", sans-serif;
    color: var(--brand-grey);
  }
  .brand-mark {
    width: 26px;
    height: 26px;
    margin-top: 8px;
    background: var(--brand-grey);
    flex: none;
  }
  .brand-name {
    font-weight: 400;
    font-size: 32px;
    line-height: 1.2;
    letter-spacing: 2px;
    text-transform: uppercase;
  }
  .brand-tagline {
    margin-top: 8px;
    font-weight: 400;
    font-size: 15px;
    letter-spacing: 1.2px;
    text-transform: uppercase;
  }
  .contact {
    position: absolute;
    right: 112px;
    text-align: right;
    font-family: "Open Sans", sans-serif;
    color: var(--text-light);
    white-space: nowrap;
  }
  .contact-email {
    top: 226px;
    font-size: 21px;
    font-weight: 400;
  }
  .contact-phone {
    top: 250px;
    font-size: 71px;
    font-weight: 800;
    line-height: 1;
    letter-spacing: -0.5px;
    text-shadow: 4px 4px 0 var(--text-shadow);
  }
  .contact-web {
    top: 330px;
    font-size: 29px;
    font-weight: 700;
    letter-spacing: 3.4px;
    line-height: 1.3;
  }
</style>
</head>
<body>
<main class="canvas">
  <section class="sign" aria-label="R Brent Construction signage">
    <svg class="sign-shapes" viewBox="0 0 1150 393" aria-hidden="true">
      <polygon class="roof" points="264,393 968,12 1150,125 1150,393" fill="var(--roof-grey)"/>
      <rect class="band" x="0" y="328" width="1150" height="41" fill="var(--band-dark)"/>
      <rect class="post" x="1103" y="0" width="24" height="393" fill="var(--band-dark)"/>
    </svg>

    <div class="brand">
      <span class="brand-mark" aria-hidden="true"></span>
      <div>
        <p class="brand-name">R Brent<br>Construction</p>
        <p class="brand-tagline">Building and Carpentry</p>
      </div>
    </div>

    <p class="contact contact-email">rbrentconstruction@mailbox-example.net</p>
    <p class="contact contact-phone">0493 518 264</p>
    <p class="contact contact-web">www.rbrentconstruction. example.net</p>
  </section>
</main>
</body>
</html>
```